New LLC consulting company needs a business card design

I need a business card design for new company in Alexandria Virginia called TK Verdant Consulting LLC. The company is focused on consulting for defense and national security issues with expertise in nuclear and space topics. I would like to see designs that are simple and I am open to colors except for brown.

Target Market(s)

All businesses that are seeking consulting help

Industry/Entity Type

Consulting

Contact Information for Business Card

Name of company - TK Verdant Consulting LLC; name (Delia Hawke) President; email: hawkedr41@mailbox-example.net; Phone: 555-271-9043

Requirements
Must have
• The details described above
Nice to have
• I'm open to all ideas
Should not have
• No brown

```html
<!DOCTYPE html>
<html lang="en">
<head>
<meta charset="utf-8">
<title>TK Verdant Consulting LLC — Business Card</title>
<link href="https://fonts.googleapis.com/css2?family=Libre+Baskerville:wght@400&family=Lato:wght@400&display=swap" rel="stylesheet">
<style>
  :root {
    --backdrop: #2a2a2a;
    --brand-blue: #0d6fb8;
    --brand-blue-light: #1183c4;
    --brand-blue-deep: #0a5ca8;
    --card-white: #ffffff;
    --ink: #1d1d1d;
    --muted: #8a8a8a;
  }
  * { box-sizing: border-box; margin: 0; padding: 0; }
  html, body {
    width: 1200px;
    height: 800px;
    overflow: hidden;
    background: var(--backdrop);
  }
  .canvas {
    width: 1200px;
    height: 800px;
    display: flex;
    align-items: center;
    justify-content: center;
    gap: 40px;
  }
  .card {
    width: 520px;
    height: 297px;
    border-radius: 16px;
    position: relative;
    box-shadow: 0 10px 24px rgba(0, 0, 0, 0.35);
  }
  .card-front {
    background: radial-gradient(ellipse at 60% 35%, var(--brand-blue-light) 0%, var(--brand-blue) 55%, var(--brand-blue-deep) 100%);
    display: flex;
    align-items: center;
    justify-content: center;
  }
  .company-name {
    font-family: "Libre Baskerville", serif;
    font-weight: 400;
    font-size: 25px;
    color: var(--card-white);
    letter-spacing: -0.3px;
  }
  .card-back {
    background: var(--card-white);
  }
  .contact-block {
    position: absolute;
    left: 62px;
    top: 128px;
  }
  .person-name {
    font-family: "Libre Baskerville", serif;
    font-weight: 400;
    font-size: 29px;
    color: var(--brand-blue);
    letter-spacing: -0.5px;
    line-height: 1;
  }
  .person-title {
    font-family: "Lato", sans-serif;
    font-size: 13px;
    letter-spacing: 0.8px;
    color: var(--muted);
    margin: 6px 0 0 12px;
  }
  .title-rule {
    width: 100px;
    height: 2px;
    background: var(--brand-blue);
    margin: 6px 0 0 24px;
  }
  .contact-list {
    list-style: none;
    margin: 22px 0 0 24px;
  }
  .contact-item {
    display: flex;
    align-items: center;
    gap: 10px;
    font-family: "Lato", sans-serif;
    font-size: 16px;
    color: var(--ink);
    line-height: 1.55;
  }
  .contact-icon {
    width: 14px;
    height: 14px;
    fill: var(--brand-blue);
    flex: none;
  }
</style>
</head>
<body>
  <main class="canvas">
    <section class="card card-front" aria-label="Card front">
      <p class="company-name">TK Verdant Consulting LLC</p>
    </section>

    <section class="card card-back" aria-label="Card back">
      <div class="contact-block">
        <h1 class="person-name">Delia Hawke</h1>
        <p class="person-title">PRESIDENT</p>
        <div class="title-rule"></div>
        <ul class="contact-list">
          <li class="contact-item">
            <svg class="contact-icon" viewBox="0 0 16 16" aria-hidden="true">
              <path d="M1 5c0-2 3-3.5 7-3.5S15 3 15 5v1.5h-3.5V5c-1-.6-2.2-.8-3.5-.8S5.5 4.4 4.5 5v1.5H1z"/>
              <path d="M4 7h8l2 7H2z"/>
              <circle cx="8" cy="10.5" r="1.8" fill="#fff"/>
            </svg>
            <span>555-271-9043</span>
          </li>
          <li class="contact-item">
            <svg class="contact-icon" viewBox="0 0 16 16" aria-hidden="true">
              <path d="M15 1 1 7l5 2 2 6z"/>
            </svg>
            <span>hawkedr41@mailbox-example.net</span>
          </li>
        </ul>
      </div>
    </section>
  </main>
</body>
</html>
```